I need a business Card Design for my practice , i am clinical herbalist. I am a herbalist specializing in Lyme disease, autism, autoimmune diseases, difficult to cure diseasesDifficult to cure diseases. In my innovative practice i link traditional medicine, herbs with science, immunologu ,pharmacology.

Industry/Entity Type

Business

Contact Information for Business Card

My company name : OSRODEK ZIELNIKA
My name : Piotr Weltak
Name of my profession : Fitoterapeuta
In Polish language Fitoterapeuta is Herbalist .

e-mail: piotrweltak@osrodekzielnika.com
www.osrodek-zielnika.pl
phone : 574 806 215
My company adress : Dąbrowa Sękowska 14 , 38-415 Mielnik
I dont have logo .

Requirements
Nice to have
• My company

```html
<!DOCTYPE html>
<html lang="pl">
<head>
<meta charset="utf-8">
<title>Osrodek Zielnika – Business Cards</title>
<link rel="stylesheet" href="https://fonts.googleapis.com/css2?family=Open+Sans:wght@400;600;700&display=swap">
<style>
  :root {
    --bg: #e6e4e0;
    --card: #ffffff;
    --ink: #111111;
    --muted: #333333;
    --green: #3bb54a;
    --rule: #555555;
  }
  * { margin: 0; padding: 0; box-sizing: border-box; }
  html, body { width: 1200px; height: 1000px; overflow: hidden; }
  body {
    background: var(--bg);
    font-family: "Open Sans", Arial, sans-serif;
    color: var(--ink);
    position: relative;
  }
  .card {
    position: absolute;
    width: 412px;
    height: 241px;
    background: var(--card);
    box-shadow: 0 3px 10px rgba(0,0,0,.18);
  }
  .card--contact { left: 210px; top: 225px; }
  .card--front { left: 452px; top: 487px; }

  .brand {
    display: flex;
    align-items: center;
    gap: 10px;
  }
  .brand__dot {
    width: 14px; height: 14px;
    border-radius: 50%;
    background: var(--green);
    flex: none;
  }
  .brand__name {
    font-weight: 600;
    color: var(--ink);
    letter-spacing: .06em;
    line-height: 1.1;
  }

  /* contact side */
  .card--contact .brand {
    position: absolute; right: 18px; top: 30px;
  }
  .card--contact .brand__name { font-size: 19px; }
  .rule {
    position: absolute; height: 1px; background: var(--rule);
  }
  .rule--top { left: 18px; right: 18px; top: 100px; }
  .person { position: absolute; left: 22px; top: 120px; }
  .person__name { font-size: 21px; font-weight: 700; line-height: 1.15; }
  .person__surname { color: var(--green); }
  .person__role { font-size: 13px; color: var(--muted); }
  .rule--contacts { left: 18px; width: 200px; top: 182px; }
  .contacts {
    position: absolute; left: 22px; top: 190px;
    list-style: none; font-size: 10.5px; color: var(--muted);
  }
  .contacts li { display: flex; align-items: center; gap: 7px; height: 14px; }
  .contacts svg { width: 10px; height: 10px; fill: var(--green); flex: none; }
  .address {
    position: absolute; right: 18px; top: 118px;
    display: flex; gap: 7px; font-size: 10.5px; color: var(--muted); line-height: 1.35;
  }
  .address svg { width: 10px; height: 13px; fill: var(--green); margin-top: 2px; }

  /* front side */
  .card--front .brand {
    position: absolute; left: 0; right: 0; top: 82px; justify-content: center;
  }
  .card--front .brand__dot { width: 18px; height: 18px; }
  .card--front .brand__name { font-size: 30px; }
  .specialty {
    position: absolute; left: 0; top: 201px;
    display: flex; align-items: center; gap: 14px; font-size: 11.5px;
  }
  .specialty__label {
    background: var(--green); color: #fff; font-weight: 600;
    padding: 2px 14px 2px 16px; width: 114px;
  }
  .specialty__list { color: var(--ink); }
</style>
</head>
<body>

  <section class="card card--contact" aria-label="Business card, contact side">
    <div class="brand">
      <span class="brand__dot"></span>
      <span class="brand__name">OSRODEK ZIELNIKA</span>
    </div>
    <div class="rule rule--top"></div>

    <div class="person">
      <h1 class="person__name">Piotr <span class="person__surname">Weltak</span></h1>
      <p class="person__role">Fitoterapeuta</p>
    </div>

    <div class="address">
      <svg viewBox="0 0 10 13"><path d="M5 0a5 5 0 0 0-5 5c0 3.5 5 8 5 8s5-4.5 5-8a5 5 0 0 0-5-5zm0 7a2 2 0 1 1 0-4 2 2 0 0 1 0 4z"/></svg>
      <p>Dąbrowa Sękowska 14<br>38-415 Mielnik</p>
    </div>

    <div class="rule rule--contacts"></div>
    <ul class="contacts">
      <li>
        <svg viewBox="0 0 10 10"><path d="M1 3.5C1 2 2.5 1 5 1s4 1 4 2.5L7.5 4.3 6.8 3H3.2l-.7 1.3zM2.5 5h5L8.5 9h-7z"/></svg>
        574 806 215
      </li>
      <li>
        <svg viewBox="0 0 10 10"><path d="M5 0a5 5 0 1 0 0 10A5 5 0 0 0 5 0zm3.9 4.5H7.2A8 8 0 0 0 6.3 1a4 4 0 0 1 2.6 3.5zM5 1.1c.6.8 1.1 2 1.2 3.4H3.8C3.9 3.1 4.4 1.9 5 1.1zM3.7 1a8 8 0 0 0-.9 3.5H1.1A4 4 0 0 1 3.7 1zM1.1 5.5h1.7A8 8 0 0 0 3.7 9a4 4 0 0 1-2.6-3.5zM5 8.9c-.6-.8-1.1-2-1.2-3.4h2.4C6.1 6.9 5.6 8.1 5 8.9zM6.3 9a8 8 0 0 0 .9-3.5h1.7A4 4 0 0 1 6.3 9z"/></svg>
        www.osrodek-zielnika.pl
      </li>
      <li>
        <svg viewBox="0 0 10 10"><path d="M0 2h10v1L5 6 0 3zm0 2l5 3 5-3v4H0z"/></svg>
        piotrweltak@osrodekzielnika.com
      </li>
    </ul>
  </section>

  <section class="card card--front" aria-label="Business card, front side">
    <div class="brand">
      <span class="brand__dot"></span>
      <span class="brand__name">OSRODEK ZIELNIKA</span>
    </div>
    <div class="specialty">
      <span class="specialty__label">Specializing In</span>
      <span class="specialty__list">Lyme Disease, Autism, Autoimmune Diseases</span>
    </div>
  </section>

</body>
</html>
```